Wedding invitation - including print files

Details
45 invitations and envelopes required

Our names: Corin and Marisol

Wedding information
Venue
At the Pennington residence, 2847 Thornbury-Waipiro road, Clevedon, Auckland for both the ceremony and reception.

Date
Saturday 19th April 2025 (Easter weekend)

Timing
Ceremony is at 3pm

Transport
A bus will pick up at 1.30pm from Linden Crest Hotel
A bus will go back to town to at 11pm and 12.15am to Linden Crest Hotel with a stop through Clevedon for those staying closer to the venue.

Accomodation
A lot of roomshares and hotels in clevedon if you wish to stay closer

Gifts
gifts aren’t necessary but a wishing well for a piece of art we will remember the day by.

Day After
We will be having some platters from 1pm on Sunday at (I will confirm this to you tomorrow sorry we are choosing between two places)

RSVP
By the 12th October 2024 to Corin 0279416652 corin@brantleygroup.co or Marisol 0278815927 marisol@quellastudio.co.nz

Here are concept ideas for the invitations and the aspects we like about them.
Three sided is practical to fit information

Font styles to use
Decorative

Colors

Designer to choose only greyscale colors for use in the design.

Requirements
Nice to have
• refer attachments and description
Should not have
• cant look cheap or tacky

```html
<!DOCTYPE html>
<html lang="en">
<head>
<meta charset="utf-8">
<title>Marisol &amp; Corin – Wedding Invitation</title>
<link href="https://fonts.googleapis.com/css2?family=Cormorant+Garamond:ital,wght@0,400;0,500;1,400&family=Pinyon+Script&display=swap" rel="stylesheet">
<style>
  :root {
    --backdrop: #d0d0d0;
    --paper: #ffffff;
    --ink: #1e1e1e;
    --ink-soft: #2e2e2e;
    --mark: #555555;
    --rule: #9a9a9a;
    --floral-dark: #6e6e6e;
    --floral-mid: #b4b4b4;
    --shadow: rgba(0,0,0,0.38);
  }
  * { box-sizing: border-box; margin: 0; padding: 0; }
  html, body { width: 799px; height: 1200px; overflow: hidden; }
  body {
    position: relative;
    background: var(--backdrop);
    font-family: "Cormorant Garamond", Georgia, serif;
    color: var(--ink);
  }

  /* Gatefold cover */
  .cover {
    position: absolute; left: 215px; top: 44px; width: 377px; height: 530px;
    background: var(--paper);
    box-shadow: 6px 6px 6px var(--shadow);
  }
  .cover__fold {
    position: absolute; left: 188px; top: 0; width: 1px; height: 100%;
    background: var(--rule);
  }
  .cover__names {
    position: absolute; left: 0; width: 100%; top: 244px;
    text-align: center;
    font-size: 24px; font-weight: 500; letter-spacing: 0.08em;
    line-height: 30px; color: var(--mark);
  }
  .cover__names span {
    background: var(--paper); padding: 6px 12px;
  }

  /* Open invitation */
  .spread {
    position: absolute; left: 20px; top: 634px; width: 759px; height: 530px;
    background: var(--paper);
    box-shadow: 6px 6px 6px var(--shadow);
  }
  .panel-rule {
    position: absolute; top: 634px; width: 1px; height: 566px;
    background: var(--rule);
  }
  .panel-rule--left { left: 210px; }
  .panel-rule--right { left: 589px; }

  .floral-corner { position: absolute; }
  .floral-corner--top {
    left: 20px; top: 634px; width: 245px; height: 172px;
    background: radial-gradient(ellipse at 30% 20%, var(--floral-dark) 0%, var(--floral-mid) 40%, rgba(255,255,255,0) 72%);
  }
  .floral-corner--bottom {
    left: 560px; top: 978px; width: 219px; height: 186px;
    background: radial-gradient(ellipse at 75% 80%, var(--floral-dark) 0%, var(--floral-mid) 40%, rgba(255,255,255,0) 72%);
  }

  .seal {
    position: absolute; left: 385px; top: 684px; width: 30px; height: 30px;
    border: 0.8px solid #666; border-radius: 50%;
  }

  .text-block { position: absolute; text-align: center; }
  .caps { text-transform: uppercase; letter-spacing: 0.06em; }
  .italic { font-style: italic; }

  .invite { left: 230px; width: 340px; color: var(--ink-soft); }
  .invite__lead { top: 750px; font-size: 12px; line-height: 19.5px; }
  .invite__lead .italic { font-size: 13px; }
  .invite__names { top: 826px; }
  .invite__name { font-size: 28px; letter-spacing: 0.07em; line-height: 34px; color: var(--ink); }
  .invite__and { font-family: "Pinyon Script", cursive; font-size: 20px; line-height: 34px; color: var(--ink-soft); }
  .invite__details { top: 962px; font-size: 13.5px; line-height: 20.5px; }
  .invite__details .caps { font-size: 12px; }
  .invite__time { top: 1043px; font-size: 12px; line-height: 16px; }
  .invite__venue { top: 1079px; font-size: 13.5px; line-height: 17px; left: 268px; width: 264px; }

  .info { font-size: 10.5px; line-height: 12.3px; color: var(--ink); }
  .info__title { font-size: 9.5px; letter-spacing: 0.04em; margin-bottom: 4px; }
  .info__body { font-style: italic; }
  .side--left { left: 46px; width: 140px; }
  .side--right { left: 615px; width: 140px; }
  .accommodation { top: 836px; }
  .gifts { top: 927px; }
  .day-after { top: 1030px; }
  .transport { top: 690px; }
  .rsvp { top: 868px; }
</style>
</head>
<body>

  <section class="cover" aria-label="Invitation cover">
    <div class="cover__fold"></div>
    <p class="cover__names"><span>Marisol &amp; Corin</span></p>
  </section>

  <section class="spread" aria-label="Invitation inside"></section>
  <div class="floral-corner floral-corner--top" role="img" aria-label="Ink drawn flowers and leaves in the top corner"></div>
  <div class="floral-corner floral-corner--bottom" role="img" aria-label="Ink drawn flowers and leaves in the bottom corner"></div>
  <div class="panel-rule panel-rule--left"></div>
  <div class="panel-rule panel-rule--right"></div>

  <div class="seal" aria-hidden="true"></div>

  <div class="text-block invite invite__lead">
    <p class="caps">It is with great joy</p>
    <p class="italic">that together</p>
    <p class="caps">with their families</p>
  </div>
  <div class="text-block invite invite__names">
    <p class="invite__name">MARISOL</p>
    <p class="invite__and">and</p>
    <p class="invite__name">CORIN</p>
  </div>
  <div class="text-block invite invite__details">
    <p class="italic">invite you to the celebration of their wedding</p>
    <p class="caps">On Saturday, the nineteenth of April</p>
    <p class="italic">two thousand twenty-five</p>
  </div>
  <div class="text-block invite invite__time">
    <p class="caps">At 3 o’clock in the afternoon</p>
  </div>
  <div class="text-block invite invite__venue">
    <p class="italic">At the Pennington residence, 2847 Thornbury-Waipiro road, Clevedon, Auckland for both the ceremony and reception</p>
  </div>

  <div class="text-block info side--left accommodation">
    <p class="info__title">ACCOMODATION</p>
    <p class="info__body">A lot of roomshares and hotels in clevedon if you wish to stay closer</p>
  </div>
  <div class="text-block info side--left gifts">
    <p class="info__title">GIFTS</p>
    <p class="info__body">gifts aren’t necessary but a wishing well for a piece of art we will remember the day by.</p>
  </div>
  <div class="text-block info side--left day-after">
    <p class="info__title">DAY AFTER</p>
    <p class="info__body">We will be having some platters from 1pm on Sunday at ...</p>
  </div>

  <div class="text-block info side--right transport">
    <p class="info__title">TRANSPORT</p>
    <p class="info__body">A bus will pick up at 1.30pm from Linden Crest Hotel<br>~<br>A bus will go back to town to at 11pm and 12.15am to Linden Crest Hotel<br>with a stop through Clevedon for those staying closer to the venue</p>
  </div>
  <div class="text-block info side--right rsvp">
    <p class="info__title">RSVP</p>
    <p class="info__body">By the 12th October 2025 to<br>Corin 0279416652<br>corin@brantleygroup.co<br>or<br>Marisol 0278815927<br>marisol@quellastudio.co.nz</p>
  </div>

</body>
</html>
```